Task and Project Management Tool Website

We need designs for both desktop and mobile for a new site, which is the marketing presentation of our new platform called Lanternfield, which is a task and project tool specific for the property sector. The name refers to people working on different workstreams on a property and crossing their paths when collaborating. The site will not do ecommerce, just a presentation of the product. We would like to include a video (no voice over) and some graphics, which we will do separately. The whole site will include a few pages, as detailed in the attach document. The product appeals to property companies and banks, hence the brand should portray reliability, corporate. We would like to see combinations of black, white and blue.
Updates

This project is currently put on hold. Client will be focusing on getting a Logo design first. Then once the logo has been created, we will resume this project and use the logo on the web designs submissions. Regards, QT Admin Barnaby

Logo design has been completed. Please resubmit and submit new web designs on this project using the logo design attached. Regards, QT Admin Barnaby

Target Market(s)

Corporate (B2B)

Logo Text

Lanternfield

Coding

Coded - Design and coding required

Number of Pages Required

5+ page

Requirements
Must have
• As in the specs
Should not have
• pictures of fake people (we prefer icons)

```html
<!DOCTYPE html>
<html lang="en">
<head>
<meta charset="utf-8">
<title>Lanternfield – Managing Property Sales With Technology</title>
<link href="https://fonts.googleapis.com/css2?family=Open+Sans:wght@400;600;700&display=swap" rel="stylesheet">
<style>
:root{
  --navy:#0a38a3;
  --navy-deep:#07308f;
  --blue:#0b84f3;
  --ink:#1d1d1f;
  --text:#333a44;
  --muted:#5b6470;
  --pale:#ebf3fd;
  --line:#e3e8ef;
  --white:#fff;
}
*{margin:0;padding:0;box-sizing:border-box}
html,body{width:1200px;height:3546px;overflow:hidden}
body{position:relative;font-family:"Open Sans",Arial,sans-serif;color:var(--text);background:var(--white)}
.abs{position:absolute}
.center{text-align:center}

/* header */
.site-header{position:absolute;left:0;top:0;width:1200px;height:77px;background:var(--white);z-index:3}
.brand{position:absolute;left:143px;top:16px;display:flex;align-items:center;gap:12px;color:var(--blue);font-size:36px;font-weight:400}
.brand-dot{width:30px;height:30px;border-radius:50%;background:var(--blue)}
.nav a{position:absolute;top:34px;font-size:14px;color:var(--text);text-decoration:none}
.nav a.active{color:var(--blue);font-weight:700}

/* hero */
.hero-band{position:absolute;left:0;top:77px;width:1200px;height:534px}
.hero-title{position:absolute;left:0;top:120px;width:1200px;text-align:center;color:var(--white);font-size:29px;font-weight:700}
.hero-lead{position:absolute;left:0;top:166px;width:1200px;text-align:center;color:var(--white);font-size:14.5px;line-height:23px;font-weight:600}
.hero-media{position:absolute;left:303px;top:231px;width:593px;height:308px;background:#e6effb;padding:9px;box-shadow:0 8px 20px rgba(10,40,110,.18)}
.hero-media div{width:100%;height:100%;background:linear-gradient(135deg,#fafcff,#eef3fa)}

/* section titles */
.section-title{position:absolute;left:0;width:1200px;text-align:center;color:var(--blue);font-size:33px;font-weight:400;line-height:1.3}

/* features */
.feature{position:absolute;width:282px;height:165px;border:1px solid var(--line);background:var(--white);text-align:center}
.feature-icon{position:absolute;left:108px;top:-33px;width:66px;height:66px;border-radius:50%;display:flex;align-items:center;justify-content:center}
.feature h3{position:absolute;left:0;top:46px;width:100%;font-size:17px;font-weight:600;color:var(--ink)}
.feature .dot{position:absolute;left:139px;top:78px;width:5px;height:5px;border-radius:50%;background:#c9ced6}
.feature p{position:absolute;left:20px;top:94px;width:240px;font-size:13px;line-height:20px;color:var(--muted)}
.feature.highlight h3,.feature.highlight p{color:var(--blue)}

/* process */
.process-bg{position:absolute;left:0;top:1219px;width:1200px;height:1017px;background:var(--pale)}
.timeline{position:absolute;left:599px;top:1383px;width:1px;height:722px;background:#c5d3e6}
.step-dot{position:absolute;left:596px;width:8px;height:8px;border-radius:50%;background:var(--blue)}
.step-card{position:absolute;width:259px;height:113px;background:var(--white)}
.step-card.left{left:305px;text-align:right}
.step-card.right{left:634px}
.step-card svg{position:absolute;top:16px}
.step-card.left svg{right:26px}
.step-card.right svg{left:26px}
.step-card h4{position:absolute;top:74px;font-size:15.5px;font-weight:600;color:var(--ink)}
.step-card.left h4{right:26px}
.step-card.right h4{left:26px}
.step-text{position:absolute;width:330px;font-size:12px;line-height:21.5px;color:var(--text)}
.step-text.right{left:637px}
.step-text.left{left:234px;text-align:right}
.btn{position:absolute;left:527px;top:2126px;width:146px;height:37px;background:var(--blue);color:var(--white);font-size:13px;font-weight:600;display:flex;align-items:center;justify-content:center;letter-spacing:.2px}

/* showcase */
.shot{position:absolute;top:2376px;width:282px;height:221px;background:#cfe3fb;padding:5px}
.shot div{width:100%;height:100%;border:2px solid #a9ccf5;background:linear-gradient(135deg,#ffffff,#f2f6fb)}
.shot-label{position:absolute;top:2612px;width:282px;text-align:center;font-size:17px;font-weight:600;color:var(--ink)}
.slider-arrow{position:absolute;top:2469px;width:32px;height:32px}

/* discover */
.discover-bg{position:absolute;left:0;top:2712px;width:1200px;height:478px;background:var(--pale)}
.offer{position:absolute;top:2927px;width:436px;height:179px;background:var(--white);box-shadow:0 4px 14px rgba(10,40,110,.06)}
.offer-icon{position:absolute;left:31px;top:-42px;width:85px;height:85px;border-radius:50%;background:var(--white);box-shadow:0 3px 10px rgba(10,40,110,.15);display:flex;align-items:center;justify-content:center}
.offer h3{position:absolute;left:28px;top:60px;font-size:25px;font-weight:700;color:var(--ink)}
.offer p{position:absolute;left:28px;top:100px;width:392px;font-size:15.5px;line-height:24px;color:var(--text)}

/* footer */
.site-footer{position:absolute;left:0;top:3190px;width:1200px;height:356px;background:linear-gradient(180deg,var(--navy),var(--navy-deep));color:var(--white)}
.footer-brand{position:absolute;left:140px;top:108px;font-size:58px;font-weight:400;color:var(--white)}
.footer-brand-dot{position:absolute;left:252px;top:36px;width:50px;height:50px;border-radius:50%;background:var(--white)}
.footer-heading{position:absolute;top:82px;font-size:17px;font-weight:400}
.footer-links{position:absolute;top:112px;list-style:none;font-size:13px}
.footer-links li{height:28px;padding-left:19px;position:relative}
.footer-links li::before{content:"›";position:absolute;left:0;top:-2px;font-size:15px}
.contact-row{position:absolute;left:867px;font-size:13px;line-height:20px}
.contact-row svg{position:absolute;left:0;top:2px}
.contact-row span{display:block;padding-left:31px}
.footer-rule{position:absolute;left:0;top:301px;width:1200px;height:1px;background:rgba(255,255,255,.18)}
.copyright{position:absolute;left:142px;top:316px;font-size:13px}
.follow{position:absolute;left:894px;top:316px;font-size:13px}
.social{position:absolute;top:310px;width:26px;height:26px;border:1.5px solid var(--white);border-radius:50%}
</style>
</head>
<body>

<header class="site-header">
  <div class="brand"><span class="brand-dot"></span>Lanternfield</div>
  <nav class="nav">
    <a style="left:629px">Home</a>
    <a style="left:713px">Product</a>
    <a class="active" style="left:809px">Fieldbid</a>
    <a style="left:914px">About</a>
    <a style="left:998px">Contacts</a>
  </nav>
</header>

<svg class="hero-band" width="1200" height="534" viewBox="0 0 1200 534">
  <polygon points="0,0 1200,0 0,534" fill="var(--navy)"/>
</svg>
<h1 class="hero-title">Managing Property Sales With Technology</h1>
<p class="hero-lead">Lanternfield is a product invented and developed by Halvergate, a London-based innovative software<br>and advisory firm founded by Owen Marlow and Luca Ferrandi.</p>
<div class="hero-media"><div role="img" aria-label="Product video or platform screenshot"></div></div>

<h2 class="section-title" style="top:640px">Features</h2>

<div class="feature highlight" style="left:142px;top:750px">
  <div class="feature-icon" style="background:#0b84f3"><svg width="30" height="30" viewBox="0 0 30 30" fill="none" stroke="#fff" stroke-width="1.6"><rect x="3" y="4" width="24" height="16" rx="1"/><path d="M11 26h8M15 20v6M10 15l6-6M13 8l4 4"/></svg></div>
  <h3>Online Auctions</h3><span class="dot"></span>
  <p>Easily set-up and run online competitive auctions</p>
</div>
<div class="feature" style="left:460px;top:750px">
  <div class="feature-icon" style="background:#1f34d8"><svg width="30" height="30" viewBox="0 0 30 30" fill="none" stroke="#fff" stroke-width="1.6"><circle cx="11" cy="18" r="5"/><circle cx="20" cy="10" r="4"/><path d="M11 10v3M11 23v3M3 18h3M16 18h3M20 3v3M20 14v3M13 10h3M24 10h3"/></svg></div>
  <h3>Agent Integration</h3><span class="dot"></span>
  <p>Allow for agents to register and invite clients to bid</p>
</div>
<div class="feature" style="left:777px;top:750px">
  <div class="feature-icon" style="background:#1fbf5f"><svg width="30" height="30" viewBox="0 0 30 30" fill="none" stroke="#fff" stroke-width="1.6"><rect x="6" y="5" width="16" height="21" rx="1"/><path d="M10 11h8M10 15h8M10 19h5M20 22l6-10"/></svg></div>
  <h3>Financing Requests</h3><span class="dot"></span>
  <p>Gather requests for financing and share them with financing partners</p>
</div>
<div class="feature" style="left:142px;top:980px">
  <div class="feature-icon" style="background:#9b13c9"><svg width="30" height="30" viewBox="0 0 30 30" fill="none" stroke="#fff" stroke-width="1.6"><circle cx="13" cy="10" r="6"/><path d="M13 16v11M17 22l4-4M13 7v6"/></svg></div>
  <h3>Buy Now Option</h3><span class="dot"></span>
  <p>In addition to real-time auctions, collect bids at fixed price</p>
</div>
<div class="feature" style="left:460px;top:980px">
  <div class="feature-icon" style="background:#f8bd1c"><svg width="30" height="30" viewBox="0 0 30 30" fill="none" stroke="#fff" stroke-width="1.6"><rect x="6" y="4" width="18" height="22" rx="1"/><path d="M10 10h10M10 14h10M10 18h6"/></svg></div>
  <h3>Automated Workflow</h3><span class="dot"></span>
  <p>All functions are automated &amp; built to create a structured &amp; efficient workflow</p>
</div>
<div class="feature" style="left:777px;top:980px">
  <div class="feature-icon" style="background:#21b3c4"><svg width="30" height="30" viewBox="0 0 30 30" fill="none" stroke="#fff" stroke-width="1.6"><circle cx="15" cy="15" r="5"/><circle cx="15" cy="15" r="10" stroke-dasharray="4 3"/></svg></div>
  <h3>Fully Customizeable</h3><span class="dot"></span>
  <p>Fieldbid can be offered in white label &amp; customized upon client’s specifications</p>
</div>

<div class="process-bg"></div>
<h2 class="section-title" style="top:1283px">How Online Property Auctions Work</h2>
<div class="timeline"></div>

<div class="step-card left" style="top:1380px">
  <svg width="46" height="46" viewBox="0 0 46 46" fill="none" stroke="var(--blue)" stroke-width="1.8"><rect x="6" y="4" width="26" height="34" rx="2"/><circle cx="19" cy="21" r="6"/><path d="M28 36l14-14"/></svg>
  <h4>Platform &amp; Process Design</h4>
</div>
<p class="step-text right" style="top:1403px">Lorem ipsum dolor sit amet, consectetuer adipiscing elit sed diam nonummy nibh euismod tincidunt ut laoreete dolore magna aliquam erat volutpat.</p>
<span class="step-dot" style="top:1432px"></span>

<p class="step-text left" style="top:1547px">Lorem ipsum dolor sit amet, consectetuer adipiscing elit sed diam nonummy nibh euismod tincidunt ut laoreete dolore magna aliquam erat volutpat.</p>
<div class="step-card right" style="top:1524px">
  <svg width="46" height="46" viewBox="0 0 46 46" fill="none" stroke="var(--blue)" stroke-width="1.8"><rect x="10" y="4" width="24" height="32" rx="2"/><path d="M22 9v14M18 12h7M18 20h7M6 30l10 10"/></svg>
  <h4>Asset Preparation</h4>
</div>
<span class="step-dot" style="top:1576px"></span>

<div class="step-card left" style="top:1668px">
  <svg width="46" height="46" viewBox="0 0 46 46" fill="none" stroke="var(--blue)" stroke-width="1.8"><path d="M6 18h8l16-9v26l-16-9H6z"/><path d="M10 26l3 10h5l-3-10M35 16c3 3 3 9 0 12"/></svg>
  <h4>Marketing</h4>
</div>
<p class="step-text right" style="top:1691px">Lorem ipsum dolor sit amet, consectetuer adipiscing elit sed diam nonummy nibh euismod tincidunt ut laoreete dolore magna aliquam erat volutpat.</p>
<span class="step-dot" style="top:1720px"></span>

<p class="step-text left" style="top:1836px">Lorem ipsum dolor sit amet, consectetuer adipiscing elit sed diam nonummy nibh euismod tincidunt ut laoreete dolore magna aliquam erat volutpat.</p>
<div class="step-card right" style="top:1813px">
  <svg width="46" height="46" viewBox="0 0 46 46" fill="none" stroke="var(--blue)" stroke-width="1.8"><path d="M18 8l12 12M14 14l8-8M24 24l8-8M22 18l16 16M4 40h20M6 34h16v6H6z"/></svg>
  <h4>Auction</h4>
</div>
<span class="step-dot" style="top:1865px"></span>

<div class="step-card left" style="top:1957px">
  <svg width="46" height="46" viewBox="0 0 46 46" fill="none" stroke="var(--blue)" stroke-width="1.8"><rect x="4" y="12" width="38" height="28" rx="2"/><path d="M15 12l8-7 8 7"/><rect x="8" y="20" width="30" height="12" rx="1"/></svg>
  <h4>Closing</h4>
</div>
<p class="step-text right" style="top:1980px">Lorem ipsum dolor sit amet, consectetuer adipiscing elit sed diam nonummy nibh euismod tincidunt ut laoreete dolore magna aliquam erat volutpat.</p>
<span class="step-dot" style="top:2009px"></span>

<a class="btn">GET IN TOUCH</a>

<h2 class="section-title" style="top:2301px">Drive Sales forward with Fieldbid</h2>
<svg class="slider-arrow" style="left:73px" viewBox="0 0 32 32" fill="none" stroke="#b5bcc6" stroke-width="1.6"><circle cx="16" cy="16" r="15"/><path d="M22 16H10M15 11l-5 5 5 5"/></svg>
<div class="shot" style="left:142px"><div role="img" aria-label="Powerful dashboard screenshot"></div></div>
<div class="shot" style="left:460px"><div role="img" aria-label="Agent area screenshot"></div></div>
<div class="shot" style="left:777px"><div role="img" aria-label="Analytical backend screenshot"></div></div>
<svg class="slider-arrow" style="left:1094px" viewBox="0 0 32 32" fill="none" stroke="var(--ink)" stroke-width="1.8"><circle cx="16" cy="16" r="15"/><path d="M10 16h12M17 11l5 5-5 5"/></svg>
<p class="shot-label" style="left:142px">Powerful Dashboard</p>
<p class="shot-label" style="left:460px">Agent Area</p>
<p class="shot-label" style="left:777px">Analytical Backend</p>

<div class="discover-bg"></div>
<h2 class="section-title" style="top:2774px">Discover the Power of Lanternfield<br>for your Organization</h2>
<div class="offer" style="left:142px">
  <div class="offer-icon"><svg width="52" height="40" viewBox="0 0 52 40" fill="none" stroke="var(--navy)" stroke-width="2"><rect x="8" y="4" width="36" height="24" rx="2"/><path d="M2 32h48l-4 5H6z"/></svg></div>
  <h3>Schedule a Demo</h3>
  <p>Let us show you how Lanternfield can enhance your operations.</p>
</div>
<div class="offer" style="left:622px">
  <div class="offer-icon"><svg width="48" height="44" viewBox="0 0 48 44" fill="none" stroke="var(--navy)" stroke-width="2"><path d="M4 16L24 3l20 13v25H4z"/><path d="M4 16l20 14 20-14M4 41l15-13M44 41L29 28"/></svg></div>
  <h3>Get a Personalized Quote</h3>
  <p>Contact us to discuss your requirements and receive a competitive quote, inclusive of a free trial period.</p>
</div>

<footer class="site-footer">
  <span class="footer-brand-dot"></span>
  <div class="footer-brand">Lanternfield</div>

  <h4 class="footer-heading" style="left:524px">Quick Links</h4>
  <ul class="footer-links" style="left:524px"><li>Home</li><li>Product</li><li>Fieldbid</li><li>About</li><li>Contacts</li></ul>
  <ul class="footer-links" style="left:644px"><li>Legal</li><li>Disclaimer</li><li>Privacy Policy</li></ul>

  <h4 class="footer-heading" style="left:867px">Contacts Details</h4>
  <div class="contact-row" style="top:112px">
    <svg width="14" height="18" viewBox="0 0 14 18" fill="none" stroke="#fff" stroke-width="1.4"><path d="M7 17s6-6 6-10A6 6 0 0 0 1 7c0 4 6 10 6 10z"/><circle cx="7" cy="7" r="2"/></svg>
    <span><b>Halvergate (UK) Ltd.</b><br>14-15 Quayside Row<br>London SE9 4QP</span>
  </div>
  <div class="contact-row" style="top:190px">
    <svg width="16" height="16" viewBox="0 0 16 16" fill="none" stroke="#fff" stroke-width="1.4"><path d="M3 1h3l1.5 4-2 1.5a9 9 0 0 0 4 4L11 8.5l4 1.5v3a2 2 0 0 1-2 2A13 13 0 0 1 1 3a2 2 0 0 1 2-2z"/></svg>
    <span>+1 555 014 2286</span>
  </div>
  <div class="contact-row" style="top:222px">
    <svg width="16" height="14" viewBox="0 0 16 14" fill="none" stroke="#fff" stroke-width="1.4"><rect x="1" y="1" width="14" height="12" rx="1"/><path d="M1 2l7 6 7-6"/></svg>
    <span>team@halvergate.example</span>
  </div>

  <div class="footer-rule"></div>
  <p class="copyright">Copyright © 2020 Lanternfield. All Rights Reserved.</p>
  <p class="follow">Follow Us</p>
  <span class="social" style="left:964px"></span>
  <span class="social" style="left:998px"></span>
  <span class="social" style="left:1032px"></span>
</footer>

</body>
</html>
```